Office Building Banner

Need a 4x8 vinyl banner made for our office/storage headquarters. Our branded colors and logo can be taken from our website, www.brightcrestroofingtx.com. All other elements of our brand have not been decided on yet, so you have creative autonomy there. Our location faces a busy highway in Seguin, Texas, so the banner needs to have our contact information and full name clearly seen from a bit away's away, hope that makes sense. Our company wants to convey attributes of strength, loyalty, protection - basically emulating the qualities of a wolf and his pack. I have uploaded a few items we have been using to date, but as you can see, graphic design is not our forte.

```html
<!DOCTYPE html>
<html lang="en">
<head>
<meta charset="utf-8">
<title>Brightcrest Roofing &amp; Renovations – Office Banner</title>
<link rel="stylesheet" href="https://fonts.googleapis.com/css2?family=Anton&family=Montserrat:wght@800&family=Roboto+Slab:wght@900&display=swap">
<style>
  :root {
    --ink: #141414;
    --night: #1d1f23;
    --ember: #ff6b45;
    --paper: #ffffff;
    --stage: #7b7b7b;
  }
  * { margin: 0; padding: 0; box-sizing: border-box; }
  html, body {
    width: 965px;
    height: 1200px;
    overflow: hidden;
    background: var(--stage);
  }
  .banner {
    position: absolute;
    left: 20px;
    top: 369px;
    width: 925px;
    height: 462px;
    overflow: hidden;
    box-shadow: 0 10px 28px rgba(0,0,0,.45);
  }
  .banner-shapes {
    position: absolute;
    inset: 0;
    width: 100%;
    height: 100%;
  }
  .headline {
    position: absolute;
    left: 37px;
    top: 22px;
    font-family: "Anton", "Impact", sans-serif;
    font-size: 100px;
    line-height: 93px;
    text-transform: uppercase;
    color: var(--paper);
    letter-spacing: -1px;
  }
  .headline .accent { color: var(--ember); }
  .website {
    position: absolute;
    left: 37px;
    top: 356px;
    font-family: "Roboto Slab", serif;
    font-weight: 900;
    font-size: 25px;
    color: var(--paper);
    text-transform: uppercase;
  }
  .phone {
    position: absolute;
    left: 37px;
    top: 394px;
    display: flex;
    align-items: center;
    gap: 16px;
  }
  .phone-icon { width: 48px; height: 48px; display: block; }
  .phone-number {
    font-family: "Montserrat", sans-serif;
    font-weight: 800;
    font-size: 50px;
    line-height: 48px;
    color: var(--ink);
    letter-spacing: -1px;
  }
  .brand {
    position: absolute;
    left: 560px;
    width: 350px;
    top: 36px;
    text-align: center;
    font-family: "Montserrat", sans-serif;
    font-weight: 800;
    color: var(--ink);
  }
  .brand-mark {
    display: block;
    width: 180px;
    height: 180px;
    margin: 0 auto 22px;
    border: 7px solid var(--ink);
    border-radius: 50%;
  }
  .brand-name { font-size: 38px; line-height: 44px; }
  .brand-line { font-size: 17px; line-height: 26px; letter-spacing: 1px; }
</style>
</head>
<body>
  <section class="banner">
    <svg class="banner-shapes" viewBox="0 0 925 462" preserveAspectRatio="none">
      <defs>
        <linearGradient id="houseTone" x1="0" y1="0" x2="0" y2="1">
          <stop offset="0" stop-color="#23262b"/>
          <stop offset="0.5" stop-color="#2e2724"/>
          <stop offset="1" stop-color="#1b1c1f"/>
        </linearGradient>
      </defs>
      <rect class="house-photo" x="0" y="0" width="925" height="339" fill="url(#houseTone)" role="img" aria-label="Dimmed photo of a two-storey house with a tiled roof"/>
      <rect class="contact-band" x="0" y="339" width="620" height="123" fill="var(--ember)"/>
      <path class="arc-border" d="M575 0 C465 80 455 270 530 339 L560 462 L925 462 L925 0 Z" fill="var(--ember)"/>
      <path class="brand-panel" d="M600 0 C495 90 490 300 615 462 L925 462 L925 0 Z" fill="var(--paper)"/>
    </svg>

    <h1 class="headline">
      Strength,<br>
      <span class="accent">Loyalt,</span><br>
      Protection
    </h1>

    <p class="website">www.brightcrestroofingtx.com</p>

    <div class="phone">
      <svg class="phone-icon" viewBox="0 0 48 48" aria-hidden="true">
        <rect width="48" height="48" rx="6" fill="var(--ink)"/>
        <path d="M14 11c-2 1-4 3-3 7 2 8 9 16 18 19 4 1 6-1 7-3l1-2-6-5-3 3c-4-2-8-6-9-10l3-3-5-6z" fill="var(--ember)"/>
        <path d="M27 12a9 9 0 0 1 9 9M27 17a4 4 0 0 1 4 4" stroke="var(--ember)" stroke-width="3" fill="none" stroke-linecap="round"/>
      </svg>
      <span class="phone-number">512-555-0148</span>
    </div>

    <div class="brand">
      <span class="brand-mark"></span>
      <div class="brand-name">BRIGHTCREST</div>
      <div class="brand-line">ROOFING &amp; RENOVATIONS</div>
    </div>
  </section>
</body>
</html>
```